Shift Haven Brochure for on call home care staffing

Brochure to describe Shift haven services. Shift haven provides after hours on-call staffing and scheduling only for home care agencies. We are 100% US Based with real agents in person answering calls. We act as an extension of their agency and integrate seamlessly. I dropped in my attempt at the brochure but my AI images suck. We want realistic images with an Americana feel. I also don't want the gold color or the same images on the new one. Feel free to redo the writing.

Target Market(s)

home care agencies

Industry/Entity Type

Health care staffing

Font styles to use
Serif
Sans Serif

Colors
0054AA
0677BA
7BADD7
CADEEF
E8F1F8

Requirements
Must have
• Catchy headlines
Nice to have
• I'd like to see professional style brochure with squares integrated in.
Should not have
• VIBRANT COLORS

```html
<!DOCTYPE html>
<html lang="en">
<head>
<meta charset="utf-8">
<title>Shift Haven – On Call Service Brochure</title>
<link rel="stylesheet" href="https://fonts.googleapis.com/css2?family=Montserrat:ital,wght@0,300;0,400;0,600;0,700;0,800;1,400;1,700&display=swap">
<style>
  :root{
    --navy:#0c3463;
    --navy-deep:#0a2b54;
    --blue:#0a4fae;
    --blue-mid:#0677ba;
    --sky:#7badd7;
    --mist:#cadeef;
    --ice:#e8f1f8;
    --paper:#ffffff;
    --stage:#f1f1f1;
    --ink:#1c2c44;
  }
  *{box-sizing:border-box;margin:0;padding:0}
  html,body{width:1200px;height:2400px;overflow:hidden;background:var(--stage);font-family:"Montserrat",sans-serif;color:var(--ink)}
  .canvas{position:relative;width:1200px;height:2400px}
  .spread{position:absolute;left:50px;width:1100px;height:850px;display:flex;box-shadow:0 18px 40px rgba(0,0,0,.14)}
  .spread--outside{top:170px}
  .spread--inside{top:1300px}
  .panel{position:relative;width:366.67px;height:100%;overflow:hidden;background:var(--paper)}
  .panel + .panel{border-left:1px solid rgba(0,0,0,.06)}
  .photo{position:absolute;left:0;right:0}
  .brand{display:flex;align-items:center;gap:10px;color:var(--navy);font-weight:800;text-transform:uppercase;letter-spacing:.04em}
  .brand__square{background:var(--navy)}
  /* outside: info panel */
  .info{background:linear-gradient(180deg,var(--blue-mid) 0%,var(--navy) 55%,var(--navy-deep) 100%);color:#fff}
  .info .photo{top:0;height:300px;background:linear-gradient(180deg,#dfe6ee 0%,#b7c6d6 50%,#3d6d9f 100%)}
  .info__body{position:absolute;top:315px;left:32px;right:32px;font-size:11.5px;line-height:1.45}
  .info__lead{font-weight:700;font-style:italic;font-size:12.5px;margin-bottom:10px}
  .info__body p + p{margin-top:9px}
  .band{background:var(--blue);color:#fff;font-weight:300;text-transform:uppercase;text-align:center;letter-spacing:.03em}
  .info .band{position:absolute;left:22px;right:22px;top:630px;padding:7px 0;font-size:17px}
  .why{position:absolute;top:685px;left:32px;list-style:none}
  .why li{display:flex;align-items:center;gap:12px;font-size:13px;font-style:italic;margin-bottom:14px}
  .dot{width:26px;height:26px;border-radius:50%;background:var(--ice);display:flex;align-items:center;justify-content:center;flex:none}
  /* outside: contact panel */
  .contact__head{position:absolute;top:40px;left:0;right:0;text-align:center}
  .contact__head .brand{justify-content:center;font-size:15px}
  .tagline{margin-top:12px;font-style:italic;font-size:16px;color:var(--navy);line-height:1.3}
  .contact .photo{top:150px;height:460px;background:linear-gradient(180deg,#f4f6f8 0%,#d9dfe6 45%,#b9c4cf 100%)}
  .contact__card{position:absolute;left:0;right:0;bottom:0;height:270px;background:var(--navy);color:#fff;text-align:center;padding-top:26px}
  .contact__card h3{font-size:17px;font-weight:600;margin-bottom:14px}
  .contact__line{font-size:12px;margin-top:6px}
  .contact__icon{display:block;margin:12px auto 0}
  .call{position:absolute;left:40px;bottom:32px;display:flex;align-items:center;gap:18px;text-align:left}
  .call__label{font-size:24px;font-weight:300;letter-spacing:.03em;line-height:1}
  .call__number{font-size:22px;font-weight:700;margin-top:4px}
  /* outside: cover */
  .cover .brand{position:absolute;top:60px;left:0;right:0;justify-content:center;font-size:30px}
  .cover .brand__square{width:34px;height:34px}
  .cover .photo{top:160px;height:450px;background:linear-gradient(180deg,#f6f7f8 0%,#e4e8ec 50%,#cdd5dd 100%)}
  .cover__title{position:absolute;left:36px;right:28px;top:565px;height:150px;background:var(--navy);color:#fff;padding:22px 36px}
  .cover__title h1{font-size:44px;line-height:.98;text-transform:uppercase}
  .cover__title .thin{font-weight:300;display:block}
  .cover__title .bold{font-weight:800;display:block}
  .cover__sub{position:absolute;left:36px;right:28px;top:715px;height:70px;background:var(--blue);color:#fff;font-size:17px;font-weight:300;text-transform:uppercase;display:flex;align-items:center;justify-content:center;letter-spacing:.03em}
  /* inside: services */
  .services{background:var(--blue)}
  .services .band{position:absolute;top:26px;left:28px;right:28px;background:var(--navy);padding:6px 0;font-size:17px}
  .services .photo{top:90px;left:20px;width:120px;height:260px;background:linear-gradient(180deg,#e8eef5 0%,#a9bfd8 60%,#c8ad8f 100%);border-radius:60px 60px 8px 8px}
  .service-list{position:absolute;top:80px;left:148px;right:20px;list-style:none;color:#fff}
  .service-list li{position:relative;padding-left:38px;margin-bottom:16px;font-size:11px;line-height:1.35}
  .service-list .dot{position:absolute;left:0;top:2px}
  .service-list strong{display:block;font-size:11.5px}
  .matters{position:absolute;top:365px;left:0;right:0;bottom:0;background:var(--ice);padding:22px 30px}
  .matters h2{font-size:19px;font-weight:400;color:var(--blue);text-transform:uppercase;margin-bottom:14px;text-align:center}
  .matters p{font-size:11.5px;line-height:1.55;text-align:justify;color:#4b5566;margin-bottom:8px}
  /* inside: staff */
  .staff{background:var(--navy)}
  .staff__text{position:absolute;top:70px;left:36px;right:36px;text-align:center;color:#fff}
  .staff__text h2{font-size:20px;font-weight:400;text-transform:uppercase;margin-bottom:14px}
  .staff__text p{font-size:12px;line-height:1.5;margin-bottom:16px}
  .staff .photo{top:380px;bottom:0;background:linear-gradient(160deg,#c99b74 0%,#e9d8cd 45%,#3c74b8 100%)}
  /* inside: expansion */
  .expand{background:var(--blue)}
  .expand__text{position:absolute;top:60px;left:32px;right:32px;color:#fff}
  .expand__text h2{font-size:22px;line-height:1.15;text-transform:uppercase;margin-bottom:16px}
  .expand__text h2 b{font-weight:800;display:block}
  .expand__text h2 span{font-weight:300;display:block}
  .expand__text p{font-size:12px;line-height:1.5}
  .expand .photo{top:330px;bottom:0;background:linear-gradient(180deg,#a57a62 0%,#7f9dc2 40%,#2c5fa6 100%)}
  .expand .call{color:#fff;left:34px;bottom:40px}
</style>
</head>
<body>
<main class="canvas">

  <section class="spread spread--outside" aria-label="Brochure outside">
    <article class="panel info">
      <div class="photo" role="img" aria-label="Photo of a smiling team of scheduling agents with headsets in a bright office"></div>
      <div class="info__body">
        <p class="info__lead">Comprehensive on-call staffing solution designed for home care by home care professionals.</p>
        <p>Experience seamless scheduling tailored to meet the unique needs of your clients and staff. Our team understands the demands of home care, ensuring that every shift is covered by qualified, compassionate caregivers. We prioritize flexibility and reliability, so you can focus on providing exceptional care while we handle the logistics.</p>
        <p>Whether you need last-minute coverage or regular scheduling support, our service is here to enhance your operation's efficiency and peace of mind. Let us help you get your weekends back and maintain the high standards your clients deserve.</p>
      </div>
      <div class="band">Why Choose Us</div>
      <ul class="why">
        <li><span class="dot"><svg width="14" height="10" viewBox="0 0 14 10"><rect width="14" height="10" fill="#0a4fae"/><rect y="2" width="14" height="2" fill="#fff"/><rect y="6" width="14" height="2" fill="#fff"/></svg></span>100% US Based</li>
        <li><span class="dot"><svg width="14" height="14" viewBox="0 0 14 14"><path d="M2 7 L7 2 L12 7 V12 H2 Z" fill="#0a4fae"/></svg></span>Home care experts</li>
        <li><span class="dot"><svg width="14" height="14" viewBox="0 0 14 14"><circle cx="7" cy="5" r="3" fill="#0a4fae"/><path d="M1 13 C2 8 12 8 13 13 Z" fill="#0a4fae"/></svg></span>Leading choice in on-call</li>
      </ul>
    </article>

    <article class="panel contact">
      <header class="contact__head">
        <div class="brand"><span class="brand__square" style="width:18px;height:18px"></span>Shift Haven</div>
        <p class="tagline">Home Care scheduling<br>by people who know home care.</p>
      </header>
      <div class="photo" role="img" aria-label="Photo of a smiling businessman and a call agent wearing a headset"></div>
      <div class="contact__card">
        <h3>Get In Touch With Us</h3>
        <p class="contact__line">dana.reyes@brightporchcare.com</p>
        <svg class="contact__icon" width="18" height="14" viewBox="0 0 18 14"><rect x="1" y="1" width="16" height="12" rx="2" fill="none" stroke="#7badd7" stroke-width="2"/><path d="M1 2 L9 8 L17 2" fill="none" stroke="#7badd7" stroke-width="2"/></svg>
        <p class="contact__line">Denton Texas</p>
        <svg class="contact__icon" width="14" height="18" viewBox="0 0 14 18"><path d="M7 1 C3 1 1 4 1 7 C1 11 7 17 7 17 C7 17 13 11 13 7 C13 4 11 1 7 1 Z" fill="#7badd7"/><circle cx="7" cy="7" r="2.5" fill="#0c3463"/></svg>
        <div class="call">
          <svg width="58" height="58" viewBox="0 0 58 58"><circle cx="29" cy="29" r="25" fill="none" stroke="#fff" stroke-width="3" stroke-dasharray="120 20"/><text x="29" y="31" fill="#fff" font-family="Montserrat,sans-serif" font-weight="800" font-size="18" text-anchor="middle">24</text><text x="29" y="42" fill="#fff" font-family="Montserrat,sans-serif" font-size="7" text-anchor="middle">HOUR</text></svg>
          <div><div class="call__label">CALL US</div><div class="call__number">555.014.2260</div></div>
        </div>
      </div>
    </article>

    <article class="panel cover">
      <div class="brand"><span class="brand__square"></span>Shift Haven</div>
      <div class="photo" role="img" aria-label="Photo of a friendly scheduling agent smiling in a bright office"></div>
      <div class="cover__title"><h1><span class="thin">On Call</span><span class="bold">Service</span></h1></div>
      <div class="cover__sub">Get Your Weekends Back</div>
    </article>
  </section>

  <section class="spread spread--inside" aria-label="Brochure inside">
    <article class="panel services">
      <div class="band">Our Services</div>
      <div class="photo" role="img" aria-label="Photo of a smiling agent talking on a phone headset"></div>
      <ul class="service-list">
        <li><span class="dot"><svg width="14" height="14" viewBox="0 0 14 14"><rect x="1" y="2" width="12" height="10" rx="1" fill="#0a4fae"/></svg></span><strong>On-Call Staffing</strong>Our dedicated staffing teams answer your calls and respond as an extension of your agency.</li>
        <li><span class="dot"><svg width="14" height="14" viewBox="0 0 14 14"><circle cx="7" cy="5" r="3" fill="#0a4fae"/><path d="M1 13 C2 8 12 8 13 13 Z" fill="#0a4fae"/></svg></span><strong>Recruiting</strong>Looking for the best caregivers? Let Shift Haven find qualified professionals for you.</li>
        <li><span class="dot"><svg width="14" height="14" viewBox="0 0 14 14"><rect x="1" y="2" width="12" height="8" fill="none" stroke="#0a4fae" stroke-width="2"/><path d="M4 12 H10" stroke="#0a4fae" stroke-width="2"/></svg></span><strong>Intake</strong>Don't miss out on new revenue with our intake services.</li>
      </ul>
      <div class="matters">
        <h2>Your Agency Matters</h2>
        <p>You will benefit from dedicated implementation staff, along with the reassurance that your agency is our highest priority. Our team is committed to understanding your unique needs and providing tailored solutions that enhance your agency's operations. From seamless onboarding to ongoing support, we ensure that every aspect of our service is designed to empower you and facilitate your success.</p>
        <p>With our expertise, you can focus on what truly matters—delivering exceptional care to your clients. Whether you're expanding your services or streamlining existing processes, we're here to support you every step of the way. Let us help you elevate your agency to new heights, ensuring both your staff and clients experience the best possible outcomes.</p>
      </div>
    </article>

    <article class="panel staff">
      <div class="staff__text">
        <h2>US Based Staff</h2>
        <p>Shift Haven is supported by U.S. based agents available 24/7.</p>
        <p><strong>Real people.<br>Real assistance.<br>Real growth.</strong></p>
        <p>Every single time.</p>
      </div>
      <div class="photo" role="img" aria-label="Photo of a caregiver sharing tea and a laugh with senior clients at a table"></div>
    </article>

    <article class="panel expand">
      <div class="expand__text">
        <h2><b>Empower</b><span>Your Agency</span><span>For Expansion</span></h2>
        <p>Shift Haven is not just an answering service; we provide a comprehensive solution for after-hours coverage. Say goodbye to expensive overtime costs and the risk of staff burnout.</p>
      </div>
      <div class="photo" role="img" aria-label="Photo of home care nurses assisting an elderly man at home"></div>
      <div class="call">
        <svg width="58" height="58" viewBox="0 0 58 58"><circle cx="29" cy="29" r="25" fill="none" stroke="#fff" stroke-width="3" stroke-dasharray="120 20"/><text x="29" y="31" fill="#fff" font-family="Montserrat,sans-serif" font-weight="800" font-size="18" text-anchor="middle">24</text><text x="29" y="42" fill="#fff" font-family="Montserrat,sans-serif" font-size="7" text-anchor="middle">HOUR</text></svg>
        <div><div class="call__label">CALL US</div><div class="call__number">555.014.2260</div></div>
      </div>
    </article>
  </section>

</main>
</body>
</html>
```